Flyer Design

We are a property company and need attractive flyers that will grab peoples attention. We want them to be bold but simple and not too busy. I attach a draft and also our logo. We will print in A5 size.
Thank you & I look forward to receiving designs.

It Company

```html
<!DOCTYPE html>
<html lang="en">
<head>
<meta charset="utf-8">
<title>Kora Developments – Subdivision Flyer</title>
<link href="https://fonts.googleapis.com/css2?family=Saira+Condensed:wght@500;700&family=Saira:wght@400&display=swap" rel="stylesheet">
<style>
  :root {
    --backdrop: #e9e7e6;
    --paper: #ffffff;
    --navy: #253d91;
    --navy-muted: #9a9fd6;
    --red: #d32129;
    --red-muted: #f4a58f;
    --brown: #7a522a;
    --deep-red: #8e1f28;
    --ink: #1d1d1d;
    --photo-light: #d9e2ec;
    --photo-mid: #8ea4bd;
    --photo-dark: #2f4866;
  }
  * { margin: 0; padding: 0; box-sizing: border-box; }
  html, body {
    width: 1200px; height: 1200px; overflow: hidden;
    background: var(--backdrop);
  }
  .flyer {
    position: absolute; left: 180px; top: 20px;
    width: 840px; height: 1160px;
    background: var(--paper);
    overflow: hidden;
    font-family: "Saira Condensed", sans-serif;
    box-shadow: 0 4px 18px rgba(0,0,0,0.18);
  }
  .hero-photo {
    position: absolute; left: 0; top: 0; width: 840px; height: 330px;
    background:
      radial-gradient(ellipse at 78% 55%, var(--photo-light) 0%, rgba(217,226,236,0) 45%),
      linear-gradient(160deg, var(--photo-dark) 0%, var(--photo-mid) 38%, var(--photo-light) 70%, var(--photo-mid) 100%);
  }
  .shapes { position: absolute; left: 0; top: 0; }
  .question {
    position: absolute; text-transform: uppercase;
    font-weight: 700; letter-spacing: 1.5px; line-height: 34px;
  }
  .question .soft { font-weight: 500; }
  .question--homeowner { left: 50px; top: 342px; font-size: 34px; color: #fff; }
  .question--homeowner .soft { color: var(--navy-muted); }
  .question--mortgage { right: 46px; top: 488px; font-size: 35px; color: #fff; text-align: right; }
  .question--mortgage .soft { color: var(--red-muted); }
  .headline {
    position: absolute; left: 42px; top: 655px;
    color: #fff; text-transform: uppercase; line-height: 52px;
    font-weight: 700;
  }
  .headline .line-small { font-size: 44px; }
  .headline .line-big { font-size: 62px; }
  .headline .soft { font-size: 46px; }
  .suitability {
    position: absolute; left: 560px; top: 745px; width: 210px;
    color: #fff; text-transform: uppercase; text-align: center;
    font-size: 22px; font-weight: 700; line-height: 28px; letter-spacing: 0.5px;
  }
  .contacts {
    position: absolute; left: 42px; top: 1036px;
    font-family: "Saira", sans-serif; font-size: 17px; color: var(--ink);
    list-style: none; line-height: 25px;
  }
  .contacts li { display: flex; align-items: center; gap: 6px; }
  .contacts svg { width: 14px; height: 14px; fill: var(--ink); }
  .brand-name {
    position: absolute; left: 440px; top: 1070px; width: 370px;
    text-align: center; color: var(--brown);
    font-size: 34px; font-weight: 700; letter-spacing: 2px; text-transform: uppercase;
  }
</style>
</head>
<body>
  <article class="flyer">
    <div class="hero-photo" role="img" aria-label="Photo of a calculator, a stock market chart and a stack of coins in cool blue tones"></div>

    <svg class="shapes" width="840" height="1160" viewBox="0 0 840 1160" aria-hidden="true">
      <defs>
        <linearGradient id="redFade" x1="0" y1="0" x2="0" y2="1">
          <stop offset="0" stop-color="#d32129"/>
          <stop offset="0.5" stop-color="#d6262e"/>
          <stop offset="1" stop-color="#f6c6c6"/>
        </linearGradient>
      </defs>
      <rect class="band-navy" x="0" y="320" width="840" height="140" fill="var(--navy)"/>
      <rect class="band-red" x="0" y="455" width="840" height="300" fill="url(#redFade)"/>
      <path class="wave-white" d="M0 640 C 90 600 170 560 260 555 C 380 550 450 690 580 700 C 680 708 760 680 840 640 L840 1160 L0 1160 Z" fill="#fff"/>
      <path class="wave-deep-red" d="M0 850 L840 890 L840 935 C 700 935 560 945 430 975 C 300 1010 150 1010 0 960 Z" fill="var(--deep-red)"/>
      <path class="wave-brown" d="M0 665 C 90 620 170 590 260 588 C 380 585 450 725 580 735 C 680 742 760 715 840 690 L840 925 C 700 915 560 920 430 945 C 300 975 150 960 0 900 Z" fill="var(--brown)"/>
    </svg>

    <p class="question question--homeowner">
      <span class="soft">Are you a</span> homeowner <span class="soft">looking for</span><br>
      financial freedom <span class="soft">while been able</span><br>
      <span class="soft">to keep</span> your own home?
    </p>

    <p class="question question--mortgage">
      <span class="soft">Are you</span> struggling<br>
      <span class="soft">to pay your</span> mortgage?
    </p>

    <h1 class="headline">
      <span class="line-small">Kora specialise in</span><br>
      <span class="line-big">Subdivisions</span><br>
      <span class="soft">including</span> <span class="line-big">finance</span><br>
      <span class="soft">and</span> <span class="line-big">management.</span>
    </h1>

    <p class="suitability">Find out if your property is suitable for subdivision in Auckland</p>

    <ul class="contacts">
      <li><svg viewBox="0 0 24 24"><path d="M6.6 10.8a15 15 0 0 0 6.6 6.6l2.2-2.2c.3-.3.7-.4 1-.2 1.1.4 2.3.6 3.6.6.6 0 1 .4 1 1V20c0 .6-.4 1-1 1A17 17 0 0 1 3 4c0-.6.4-1 1-1h3.5c.6 0 1 .4 1 1 0 1.3.2 2.5.6 3.6.1.3 0 .7-.2 1z"/></svg>021 555 0142</li>
      <li><svg viewBox="0 0 24 24"><path d="M2 5h20v14H2z M2 5l10 8 10-8" fill="none" stroke="#1d1d1d" stroke-width="2.4"/></svg>info@korasubdivisions.com</li>
      <li><svg viewBox="0 0 24 24"><circle cx="12" cy="12" r="9.5" fill="none" stroke="#1d1d1d" stroke-width="2"/><path d="M2.5 12h19M12 2.5c3 3 3 16 0 19M12 2.5c-3 3-3 16 0 19" fill="none" stroke="#1d1d1d" stroke-width="1.6"/></svg>www.korasubdivisions.com</li>
    </ul>

    <p class="brand-name">Kora Developments</p>
  </article>
</body>
</html>
```